Harbor Current LLC

I need a business card containing the following:

HarborCurrentLLC
Certified Master Electrician
Licensed and insured
"powered by excellence"

Dale Horvath. Brian Okafor
555-014-2281 555-019-6640

HarborCurrentLLC.example

red white and blue color scheme

Industry/Entity Type

Electric Company

Contact Information for Business Card

Red white and blue coloring

Colors
ec1f27
0456a4
ffffff

Requirements
Must have
• Harbor Current
• Certified master Electrician
• Liscensed and insured
• "Powered by excellence"
• Dale Horvath. 5550142281
• Brian Okafor. 5550196640

```html
<!DOCTYPE html>
<html lang="en">
<head>
<meta charset="utf-8">
<title>Harbor Current LLC – Business Card</title>
<link rel="stylesheet" href="https://fonts.googleapis.com/css2?family=PT+Sans+Narrow:wght@700&family=Source+Sans+3:wght@400;600&display=swap">
<style>
  :root {
    --backdrop: #ecedef;
    --card: #ffffff;
    --red: #ec1f27;
    --blue: #0456a4;
    --ink: #1f2a44;
    --text: #3e3e42;
    --soft-shadow: rgba(0, 0, 0, 0.12);
  }
  * { box-sizing: border-box; margin: 0; padding: 0; }
  html, body {
    width: 1200px;
    height: 800px;
    overflow: hidden;
    background: var(--backdrop);
  }
  .canvas {
    position: relative;
    width: 1200px;
    height: 800px;
  }
  .card {
    position: absolute;
    left: 75px;
    top: 100px;
    width: 1050px;
    height: 600px;
    background: var(--card);
    overflow: hidden;
    box-shadow: 0 10px 30px var(--soft-shadow);
    font-family: "Source Sans 3", "Myriad Pro", sans-serif;
    color: var(--text);
  }
  .card-shapes {
    position: absolute;
    inset: 0;
    width: 1050px;
    height: 600px;
  }
  .shape-accent { fill: var(--red); }
  .shape-dark { fill: var(--blue); }

  .brand {
    position: absolute;
    left: 48px;
    top: 92px;
    display: flex;
    align-items: center;
    gap: 16px;
  }
  .brand-square {
    width: 54px;
    height: 54px;
    background: var(--blue);
  }
  .brand-name {
    font-size: 44px;
    font-weight: 600;
    color: var(--blue);
    letter-spacing: 0.5px;
  }

  .tagline {
    position: absolute;
    left: 48px;
    top: 208px;
    font-family: "PT Sans Narrow", "Myriad Pro Condensed", sans-serif;
    font-weight: 700;
    font-size: 40px;
    color: var(--ink);
  }

  .people {
    position: absolute;
    left: 48px;
    top: 268px;
    font-size: 34px;
    line-height: 40px;
    font-weight: 600;
  }
  .person-primary { color: var(--red); }
  .person-secondary { color: var(--blue); }

  .contact-list {
    position: absolute;
    left: 52px;
    top: 372px;
    list-style: none;
    font-size: 31px;
    line-height: 48px;
    color: var(--text);
  }
  .contact-list li {
    display: flex;
    align-items: center;
    gap: 18px;
  }
  .contact-icon {
    width: 22px;
    height: 22px;
    flex: none;
  }
  .contact-icon .disc { fill: var(--red); }
  .contact-icon .glyph { fill: none; stroke: #fff; stroke-width: 1.6; stroke-linecap: round; }
  .contact-icon .glyph-fill { fill: #fff; }

  .credentials {
    position: absolute;
    left: 640px;
    top: 350px;
    font-size: 29px;
    line-height: 36px;
    color: var(--text);
  }
</style>
</head>
<body>
<main class="canvas">
  <article class="card">
    <svg class="card-shapes" viewBox="0 0 1050 600" aria-hidden="true">
      <path class="shape-accent" d="M520,0 C548,62 575,84 640,84 L905,84 L990,0 Z"/>
      <path class="shape-dark" d="M0,582 L250,582 L232,600 L0,600 Z"/>
      <path class="shape-accent" d="M238,600 C262,562 290,552 340,552 L842,552 L892,510 L1050,510 L1050,600 Z"/>
      <path class="shape-dark" d="M896,506 L915,490 L1050,490 L1050,506 Z"/>
    </svg>

    <div class="brand">
      <span class="brand-square"></span>
      <span class="brand-name">Harbor Current LLC</span>
    </div>

    <p class="tagline">“Powered by excellence”</p>

    <div class="people">
      <p class="person-primary">Dale Horvath</p>
      <p class="person-secondary">Brian Okafor</p>
    </div>

    <ul class="contact-list">
      <li>
        <svg class="contact-icon" viewBox="0 0 22 22" aria-hidden="true">
          <circle class="disc" cx="11" cy="11" r="11"/>
          <path class="glyph-fill" d="M7.2,5.5 L9.2,5.5 L10,8.3 L8.8,9.4 C9.6,11 11,12.4 12.6,13.2 L13.7,12 L16.5,12.8 L16.5,14.8 C16.5,15.6 15.8,16.2 15,16.1 C10.2,15.6 6.4,11.8 5.9,7 C5.8,6.2 6.4,5.5 7.2,5.5 Z"/>
        </svg>
        <span>555-014-2281</span>
      </li>
      <li>
        <svg class="contact-icon" viewBox="0 0 22 22" aria-hidden="true">
          <circle class="disc" cx="11" cy="11" r="11"/>
          <rect class="glyph" x="7.5" y="4.5" width="7" height="13" rx="1.5"/>
          <path class="glyph" d="M10,15 L12,15"/>
        </svg>
        <span>555-019-6640</span>
      </li>
      <li>
        <svg class="contact-icon" viewBox="0 0 22 22" aria-hidden="true">
          <circle class="disc" cx="11" cy="11" r="11"/>
          <circle class="glyph" cx="11" cy="11" r="6"/>
          <ellipse class="glyph" cx="11" cy="11" rx="2.6" ry="6"/>
          <path class="glyph" d="M5,11 L17,11"/>
        </svg>
        <span>www.HarborCurrentLLC.example</span>
      </li>
    </ul>

    <div class="credentials">
      <p>HarborCurrent</p>
      <p>Certified Master Electrician</p>
      <p>Licensed and insured</p>
    </div>
  </article>
</main>
</body>
</html>
```